Business Card Design Project

business cards to match the logo design reference 1970674
specific details to be provided asap - message to follow
hello - thank you for the logo design (reference 1970674) which we are very happy with. In terms of business cards you presented a couple of options ie blue front/white back and then the reverse. Can we start with the white front version but change the text details to black font?
Actual details are as follows;
Dorian Plimsoll
Managing Director
e dorianplimsoll@kestrowe.com.au
t +61 2 5550 1937
m +61 400 555 219
Suite 712, Level 7, 48 Thornbury Rd
Sydney, NSW 2000, Australia
www.kestrowe.com.au

```html
<!DOCTYPE html>
<html lang="en">
<head>
<meta charset="utf-8">
<title>Kestrowe – Business Card</title>
<link href="https://fonts.googleapis.com/css2?family=Jost:wght@400;500&display=swap" rel="stylesheet">
<style>
  :root {
    --page-bg: #ffffff;
    --card-bg: #ffffff;
    --card-border: #e6e7e8;
    --brand-blue: #2a9fdc;
    --brand-grey: #6d6e70;
    --ink: #111111;
  }
  html, body {
    margin: 0;
    padding: 0;
    width: 1200px;
    height: 1000px;
    overflow: hidden;
    background: var(--page-bg);
  }
  .canvas {
    position: relative;
    width: 1200px;
    height: 1000px;
    font-family: "Jost", "Futura", sans-serif;
    color: var(--ink);
  }
  .card {
    position: absolute;
    left: 72px;
    top: 198px;
    width: 1049px;
    height: 597px;
    border: 3px solid var(--card-border);
    background: var(--card-bg);
  }
  .brand {
    position: absolute;
    left: 0;
    right: 0;
    top: 80px;
    display: flex;
    justify-content: center;
    align-items: center;
    gap: 34px;
  }
  .brand-mark {
    width: 130px;
    height: 130px;
    border-radius: 50%;
    background: var(--brand-blue);
  }
  .brand-name {
    font-weight: 500;
    font-size: 96px;
    line-height: 1;
    color: var(--brand-grey);
    letter-spacing: 1px;
  }
  .person {
    position: absolute;
    left: 0;
    right: 0;
    top: 328px;
    text-align: center;
  }
  .person-name {
    margin: 0;
    font-weight: 400;
    font-size: 42px;
    line-height: 1.2;
  }
  .person-title {
    margin: 6px 0 0;
    font-weight: 400;
    font-size: 25px;
    line-height: 1.2;
  }
  .contact {
    position: absolute;
    left: 0;
    right: 0;
    top: 500px;
    text-align: center;
    font-size: 21.5px;
    line-height: 34px;
    letter-spacing: 0.2px;
  }
  .contact p { margin: 0; }
  .contact .gap { display: inline-block; width: 12px; }
</style>
</head>
<body>
  <main class="canvas">
    <section class="card">
      <div class="brand">
        <div class="brand-mark" aria-hidden="true"></div>
        <div class="brand-name">Kestrowe</div>
      </div>

      <div class="person">
        <h1 class="person-name">Dorian Plimsoll</h1>
        <p class="person-title">Managing Director</p>
      </div>

      <address class="contact" style="font-style: normal;">
        <p>e dorianplimsoll@kestrowe.com.au<span class="gap"></span>t +61 2 5550 1937<span class="gap"></span>m +61 400 555 219</p>
        <p>Suite 712, Level 7, 48 Thornbury Rd<span class="gap"></span>Sydney, NSW 2000, Australia<span class="gap"></span>www.kestrowe.com.au</p>
      </address>
    </section>
  </main>
</body>
</html>
```